IT Consultancy Needs Daring Webpage (uncoded)

We are looking for a web page for a small IT firm, Kestrel Networking. We provide remote IT services, website development and IT consultancy. We are looking for a website that is a bit unique and will look both professional and cutting edge.

We are mainly targeting high cash flow small businesses.
Feel free to play with our yellow/blue theme. We where aiming for similar colours to movie posters i.e the Garnet Cipher, http://lnkbx.example/q8Vwm. Think metallic, flashy and classy like a colourful zuTab.
Updates

We have a website but it is very poor and we would prefer if you did not use it for inspiration.

We quite like this design http://browse.pixmosaicly.example/designs/web/?order=24&offset=24#/k7m3pw9

The three cornerstones of our business are Consult, Support and E-Marketing

other designs are welcome as well (different from the the link above)

Target Market(s)

Small Businesses

Industry/Entity Type

Movie

Requirements
Must have
• Space for Home, Services, Contact and Blog menu bars.

Our logo is ok, you are welcome to adjust it a little to meet your needs.

While we appreciate most websites have a dense middle ground for navigation panels, we would like the most important buttons highlighted as well as a slightly interesting background for example, instead of a plain colour background, a slight hint of a pattern or image.
Should not have
• Should not have a banner.

```html
<!DOCTYPE html>
<html lang="en">
<head>
<meta charset="utf-8">
<title>Kestrel Networking</title>
<link rel="stylesheet" href="https://fonts.googleapis.com/css2?family=Arimo:wght@400;700&family=Open+Sans:wght@400;600&display=swap">
<style>
:root{
  --amber:#fdb214;
  --navy:#131b40;
  --navy-mid:#1e2a58;
  --paper:#e8e9e8;
  --ink:#111;
  --link:#1a8fd0;
  --rule:#b9b9b9;
  --white:#fff;
}
*{margin:0;padding:0;box-sizing:border-box}
html,body{width:1200px;height:1000px;overflow:hidden}
body{position:relative;background:linear-gradient(#d9dcda 410px,var(--paper) 620px);font-family:"Arimo",Arial,sans-serif;color:var(--ink)}
.site-header{position:absolute;left:0;top:0;width:1200px;height:71px;background:var(--amber);border-bottom:1px solid #fbe7b5}
.brand-name{position:absolute;left:130px;top:21px;font-family:"Open Sans",sans-serif;font-size:21px;font-weight:400;color:var(--ink);letter-spacing:.3px;line-height:28px}
.main-nav a{position:absolute;top:26px;font-size:14px;line-height:16px;color:var(--white);text-decoration:none}
.nav-sep{position:absolute;top:28px;width:1px;height:14px;background:var(--white)}
.hero{position:absolute;left:0;top:71px;width:1200px;height:340px;background:radial-gradient(ellipse at 50% 55%,var(--navy-mid),var(--navy) 70%);border-bottom:2px solid #f2f2f2}
.hero-title{position:absolute;top:28px;width:100%;text-align:center;font-family:"Open Sans",sans-serif;font-weight:600;font-size:35px;color:var(--white)}
.pillar{position:absolute;top:92px;width:150px;text-align:center;color:var(--white);font-family:"Open Sans",sans-serif}
.pillar svg{display:block;margin:0 auto}
.pillar h2{font-weight:400;font-size:21px;line-height:28px;margin-top:16px}
.pillar p{width:132px;margin:3px auto 0;font-size:11px;line-height:14.5px}
.pillar .cta{display:inline-block;margin-top:25px;width:80px;height:30px;line-height:28px;font-size:13px;background:linear-gradient(#2a2a2a,#000);border:1px solid #444;border-radius:2px;color:var(--white)}
.col{position:absolute;top:433px;font-size:12px;line-height:14.5px}
.col h3{font-weight:400;font-size:18px;line-height:22px;color:var(--amber);margin-bottom:25px}
.col p+p{margin-top:14px}
.tweet{font-size:11px;line-height:13px;margin-bottom:14px}
.tweet .handle{color:var(--link)}
.tweet .url{color:var(--link);text-decoration:underline}
.rule{position:absolute;left:120px;width:960px;height:3px;background:var(--rule)}
.fcol{position:absolute;top:717px;font-size:11px}
.fcol h4{font-weight:400;font-size:18px;line-height:22px;color:#444;margin-bottom:15px}
.fcol a{display:block;color:#333;text-decoration:underline;margin-bottom:10px;line-height:14px}
.social{display:flex;gap:10px}
.social span{width:35px;height:35px;border-radius:50%;background:radial-gradient(circle at 40% 35%,#fff,#bbb);border:1px solid #999}
.contact-row{display:flex;align-items:center;gap:8px;margin-bottom:12px;font-size:11px;white-space:nowrap}
.copyright{position:absolute;top:912px;width:100%;text-align:center;font-size:11px;color:#444}
</style>
</head>
<body>
<header class="site-header">
  <span class="brand-name">KESTREL NETWORKING</span>
  <nav class="main-nav">
    <a href="#" style="left:558px">Home</a><span class="nav-sep" style="left:623px"></span>
    <a href="#" style="left:653px">Services</a><span class="nav-sep" style="left:736px"></span>
    <a href="#" style="left:766px">Support</a><span class="nav-sep" style="left:845px"></span>
    <a href="#" style="left:875px">Contact</a><span class="nav-sep" style="left:953px"></span>
    <a href="#" style="left:983px">Blog</a>
  </nav>
</header>

<section class="hero" role="img" aria-label="Faint harbour skyline photo with grid overlay in deep navy tones">
  <h1 class="hero-title">Big business IT for small businesses</h1>
  <div class="pillar" style="left:315px">
    <svg width="50" height="46" viewBox="0 0 50 46"><rect x="17" y="2" width="16" height="8" rx="3" fill="none" stroke="#fff" stroke-width="3"/><rect x="2" y="9" width="46" height="33" rx="5" fill="#f0f0f0"/><line x1="2" y1="22" x2="48" y2="22" stroke="#9aa" stroke-width="1.5"/><circle cx="16" cy="22" r="3" fill="#555"/><circle cx="34" cy="22" r="3" fill="#555"/></svg>
    <h2>Consult</h2>
    <p>Lorem ipsum dolor sit amet, consectetur adipiscing elit. Sed rutrum interdum tortor.</p>
    <span class="cta">Learn more</span>
  </div>
  <div class="pillar" style="left:516px">
    <svg width="50" height="46" viewBox="0 0 50 46"><path d="M8 4a10 10 0 0 0 12 13l20 22a4 4 0 0 0 6-6L24 13A10 10 0 0 0 11 1l6 6-3 6-6-3z" fill="#f0f0f0"/></svg>
    <h2>Support</h2>
    <p>Lorem ipsum dolor sit amet, consectetur adipiscing elit. Sed rutrum interdum tortor.</p>
    <span class="cta">Learn more</span>
  </div>
  <div class="pillar" style="left:718px">
    <svg width="50" height="46" viewBox="0 0 50 46"><path d="M4 2h30a3 3 0 0 1 3 3v18a3 3 0 0 1-3 3H14l-8 7v-7H4a3 3 0 0 1-3-3V5a3 3 0 0 1 3-3z" fill="#f0f0f0"/><path d="M40 12h5a3 3 0 0 1 3 3v16a3 3 0 0 1-3 3h-2v8l-8-8H22a3 3 0 0 1-3-3v-2h18a3 3 0 0 0 3-3z" fill="#d8d8d8"/></svg>
    <h2>e-Marketing</h2>
    <p>Lorem ipsum dolor sit amet, consectetur adipiscing elit. Sed rutrum interdum tortor.</p>
    <span class="cta">Learn more</span>
  </div>
</section>

<section class="col" style="left:130px;width:268px">
  <h3>About Us</h3>
  <p>Kestrel Networking provides fast, efficient consultation and remote IT support. Our focus is personalised solutions ensuring we meet your needs.</p>
</section>
<section class="col" style="left:430px;width:300px">
  <h3>Featured Service</h3>
  <p>- Lorem ipsum dolor sit amet, consectetur adipiscing elit. Duis egestas, magna at elementum eleifend, ante leo pellentesque nulla, vel scelerisque diam elit vel est. Aliquam laoreet velit ut est consequat interdum.</p>
  <p>- Praesent volutpat est luctus turpis viverra lobortis. Vestibulum quis erat purus, vel adipiscing nibh. Ut mattis justo eu quam mollis sed tempor ligula adipiscing.</p>
</section>
<section class="col" style="left:770px;width:310px">
  <h3>On Chirper</h3>
  <p class="tweet"><span class="handle">@KestrelNetwork</span> Lorem ipsum dolor sit amet, consectetur adipiscing elit. <span class="url">http://lnkbx.ex/r4Tz8</span></p>
  <p class="tweet"><span class="handle">@KestrelNetwork</span> Fusce sed ipsum quis nisl mollis bibendum. Proin rutrum eleifend urna a gravida. <span class="url">http://lnkbx.ex/r4Tz8</span></p>
  <p class="tweet"><span class="handle">@KestrelNetwork</span> Cras massa sapien, dictum at ullamcorper quis, sodales a lorem. <span class="url">http://lnkbx.ex/r4Tz8</span></p>
</section>

<div class="rule" style="top:700px"></div>
<footer>
  <div class="fcol" style="left:130px"><h4>Our Company</h4><a href="#">Home</a><a href="#">Services</a><a href="#">Support</a><a href="#">Contact</a><a href="#">Blog</a></div>
  <div class="fcol" style="left:370px"><h4>Security &amp; Privacy</h4><a href="#">Sitemap</a><a href="#">Privacy Policy</a><a href="#">Terms of Service</a><a href="#">Live Help etc</a></div>
  <div class="fcol" style="left:610px"><h4>Stay In Touch</h4><div class="social"><span></span><span></span><span></span><span></span></div></div>
  <div class="fcol" style="left:850px"><h4>Need Help?</h4>
    <div class="contact-row"><svg width="22" height="16" viewBox="0 0 22 16"><rect x="1" y="1" width="20" height="14" fill="#ccc" stroke="#888"/><path d="M1 1l10 8 10-8" fill="none" stroke="#777"/></svg><span><b>E-Mail:</b> sales@kestrelnet.example</span></div>
    <div class="contact-row"><svg width="22" height="18" viewBox="0 0 22 18"><path d="M5 1l4 4-2 3c1 3 3 5 6 6l3-2 4 4-3 2C9 17 3 11 2 4z" fill="#999"/></svg><span><b>Phone:</b> 0412 555 318</span></div>
  </div>
</footer>
<div class="rule" style="top:890px"></div>
<p class="copyright">Copyright © 2011 Kestrel Networking LLC All Right Reserved.</p>
</body>
</html>
```